Virtual Reality immersive experiences

Print ad 8.5" X 11"
Advertising to have people come rent time in our virtual reality room.
Fun for all ages
Unique experience
Immersive experience into 3D world
Escape reality
Be at heart of action - bottom of the ocean, travel the world, fight the invaders, solve the mystery and so much more
System used is Brelvo Optra
Dedicated room
Family friendly
$24 half hour
$40 per hour
Updates

Industry/Entity Type

Advertising

Requirements
Must have
• Be fun looking
• Eye catching
• Great pictures of VR experiences
• Pricing is $24 / 30 minutes and $40 / 1 hour
• Our location: 587 Larch Avenue, Three Hills, Alberta
• Our contact: 403-618-2093
• I have attached TERMALDO Technology Solutions logo which should be somewhere on the ad.
Nice to have
• could use phrases like: travel the world, explore the ocean depths, fight the invaders, visit the carnival

```html
<!DOCTYPE html>
<html lang="en">
<head>
<meta charset="utf-8">
<title>Virtual Reality Room – Print Ad</title>
<link href="https://fonts.googleapis.com/css2?family=Orbitron:wght@500;700&display=swap" rel="stylesheet">
<style>
  :root {
    --backdrop: #808080;
    --ink-dark: #050608;
    --ink-white: #ffffff;
    --accent-gold: #f5c210;
    --space-deep: #0a1a3c;
    --space-blue: #2f6fc0;
    --space-glow: #8fc4f2;
    --ember: #c7801e;
    --footer-bg: #ffffff;
    --logo-ink: #1a1a1a;
  }
  html, body {
    margin: 0;
    width: 1200px;
    height: 1000px;
    overflow: hidden;
    background: var(--backdrop);
  }
  .ad {
    position: absolute;
    left: 427px;
    top: 277px;
    width: 345px;
    height: 446px;
    background: var(--ink-dark);
    overflow: hidden;
    font-family: "Orbitron", sans-serif;
    color: var(--ink-white);
  }
  .hero-visual {
    position: absolute;
    left: 0; top: 0;
    width: 345px; height: 278px;
    background:
      radial-gradient(circle at 12% 8%, var(--ember) 0%, transparent 28%),
      radial-gradient(circle at 40% 35%, var(--space-glow) 0%, transparent 35%),
      radial-gradient(ellipse at 50% 80%, var(--space-blue) 0%, transparent 60%),
      linear-gradient(180deg, var(--space-deep) 0%, #1b3f7a 55%, #3a3e48 100%);
  }
  .headline-band {
    position: absolute;
    left: 0; top: 8px;
    width: 345px; height: 40px;
    background: rgba(0,0,0,0.55);
  }
  .headline {
    position: absolute;
    left: 12px; top: 12px;
    margin: 0;
    font-size: 27px;
    font-weight: 700;
    letter-spacing: 0.5px;
    white-space: nowrap;
    line-height: 30px;
  }
  .headline-box {
    position: absolute;
    right: 2px; top: 50px;
    width: 113px; height: 38px;
    background: var(--ink-dark);
    font-size: 27px;
    font-weight: 700;
    line-height: 38px;
    text-align: right;
    padding-right: 10px;
    box-sizing: border-box;
  }
  .pitch {
    position: absolute;
    left: 12px; top: 290px;
    width: 325px;
    margin: 0;
    font-size: 8.6px;
    line-height: 12px;
    font-weight: 500;
  }
  .pitch .lead { color: var(--accent-gold); }
  .features {
    position: absolute;
    left: 12px; top: 325px;
    margin: 0; padding: 0;
    list-style: none;
    font-size: 8.6px;
    line-height: 11px;
    font-weight: 500;
  }
  .pricing {
    position: absolute;
    left: 236px; top: 324px;
    font-size: 12.5px;
    font-weight: 700;
    line-height: 18px;
  }
  .pricing .amount { color: var(--accent-gold); }
  .phone {
    position: absolute;
    left: 12px; top: 384px;
    font-size: 11px;
    font-weight: 700;
  }
  .phone .number { color: var(--accent-gold); }
  .address {
    position: absolute;
    left: 12px; top: 402px;
    font-size: 8.6px;
    font-weight: 700;
    color: var(--accent-gold);
  }
  .footer-strip {
    position: absolute;
    left: 0; top: 420px;
    width: 345px; height: 26px;
    background: var(--footer-bg);
  }
  .brand {
    position: absolute;
    left: 10px; top: 426px;
    font-size: 8px;
    font-weight: 700;
    color: var(--logo-ink);
    line-height: 9px;
  }
  .brand small {
    display: block;
    font-size: 3.4px;
    font-weight: 700;
    letter-spacing: 0.3px;
  }
  .product-visual {
    position: absolute;
    left: 228px; top: 376px;
    width: 117px; height: 68px;
    background: radial-gradient(ellipse at 50% 55%, #2a2a2e 0%, #121214 60%, rgba(255,255,255,0) 100%);
  }
</style>
</head>
<body>
  <main class="ad">
    <div class="hero-visual" role="img" aria-label="Photo of a person wearing a VR headset holding motion controllers, set against Earth and glowing space scenery"></div>
    <div class="headline-band"></div>
    <h1 class="headline">VIRTUAL REALITY</h1>
    <div class="headline-box">ROOM</div>

    <p class="pitch"><span class="lead">Be at heart of action</span> – bottom of the ocean, travel the world, fight the invaders, solve the mystery and so much more</p>

    <ul class="features">
      <li>System used Brelvo Optra</li>
      <li>Dedicated room</li>
      <li>Family friendly</li>
    </ul>

    <div class="pricing">
      <div><span class="amount">$24</span> half hour</div>
      <div><span class="amount">$40</span> per hour</div>
    </div>

    <div class="phone">PHONE: <span class="number">403-618-2093</span></div>
    <div class="address">587 Larch Avenue, Three Hills, Alberta</div>

    <div class="footer-strip"></div>
    <div class="brand">TERMALDO<small>TECHNOLOGY SOLUTIONS</small></div>

    <div class="product-visual" role="img" aria-label="Product photo of the black VR headset with cable"></div>
  </main>
</body>
</html>
```